Letterhead design for Dental Practice - Ashby Lane Dental Care

Letterhead for Private Dental Practice. To be used for all official correspondance and for printing treatment details on to be given to patients.

Target Market(s)

Private dental patients

Industry/Entity Type

Dental Clinic

Font styles to use
Other font styles liked:
• nexa-light

Colors
33a6d7
1c66ac
85abd2

Requirements
Must have
• info in the footer and header needs to be 3.5cm from upper/lower boader of paper, see photo in uploaded files
• info details:
• tel. 0115 947 3051
• email info@ashbylanedc.co.uk
• ashbylanedentalcare.co.uk
• 17b Ashby Lane West Bridgford Nottingham NG2 7QT
• nexa-light font as in uploaded logo files
Should not have
• No funny tooth pictures

```html
<!DOCTYPE html>
<html lang="en">
<head>
<meta charset="utf-8">
<title>Ashby Lane Dental Care – Letterhead</title>
<link rel="stylesheet" href="https://fonts.googleapis.com/css2?family=Open+Sans:wght@300;400&display=swap">
<style>
  :root {
    --blue-dark: #1c66ac;
    --blue-bright: #33a6d7;
    --blue-soft: #85abd2;
    --blue-faint: #e3edf6;
    --ink: #2b2b2b;
    --paper: #ffffff;
  }
  * { box-sizing: border-box; margin: 0; padding: 0; }
  html, body {
    width: 865px; height: 1200px; overflow: hidden;
    background: var(--paper);
    font-family: "Open Sans", Arial, sans-serif;
    color: var(--ink);
  }
  .letterhead { position: relative; width: 865px; height: 1200px; overflow: hidden; }

  /* Header */
  .header-bar { position: absolute; top: 96px; height: 10px; background: var(--blue-dark); }
  .header-bar--left { left: 0; width: 55px; }
  .header-bar--right { left: 350px; right: 0; }
  .header-rule { position: absolute; top: 112px; left: 350px; right: 0; height: 1px; background: var(--blue-soft); }

  .brand { position: absolute; top: 40px; left: 70px; width: 222px; text-align: center; }
  .brand-dot { display: block; width: 34px; height: 34px; margin: 0 auto 12px; border-radius: 50%; background: var(--blue-bright); }
  .brand-name { font-weight: 300; font-size: 19px; letter-spacing: 0.5px; color: var(--blue-bright); white-space: nowrap; }

  .brand-watermark {
    position: absolute; top: 150px; left: 470px;
    font-weight: 300; font-size: 72px; line-height: 0.95;
    color: var(--blue-faint); white-space: nowrap; pointer-events: none;
  }

  /* Letter body */
  .letter { position: absolute; top: 300px; left: 102px; width: 662px; font-size: 15px; line-height: 28px; }
  .recipient { line-height: 21px; margin-bottom: 28px; }
  .letter p.body-copy { text-align: justify; margin-bottom: 20px; }
  .signoff { margin-top: 26px; line-height: 21px; }
  .signature { display: block; width: 110px; height: 26px; margin-bottom: 4px; background: linear-gradient(90deg, #d6d6d6, #ececec); border-radius: 3px; }

  /* Footer */
  .footer-row { position: absolute; left: 0; right: 0; height: 44px; }
  .footer-row--top { top: 1078px; }
  .footer-row--bottom { top: 1136px; }
  .icon-block { position: absolute; top: 0; width: 96px; height: 44px; background: var(--blue-dark); display: flex; align-items: center; justify-content: center; }
  .icon-block--left { left: 0; }
  .icon-block--right { right: 0; width: 107px; }
  .icon-block svg { width: 20px; height: 20px; }
  .footer-rule { position: absolute; bottom: 0; height: 2px; background: var(--blue-dark); width: 240px; }
  .footer-rule--left { left: 96px; }
  .footer-rule--right { right: 107px; }
  .footer-text { position: absolute; top: 0; height: 42px; display: flex; flex-direction: column; justify-content: center; font-size: 14px; line-height: 18px; }
  .footer-text--left { left: 110px; }
  .footer-text--right { right: 122px; text-align: right; }
  .base-bar { position: absolute; left: 0; bottom: 0; width: 96px; height: 8px; background: var(--blue-dark); }
</style>
</head>
<body>
<main class="letterhead">
  <div class="header-bar header-bar--left"></div>
  <div class="header-bar header-bar--right"></div>
  <div class="header-rule"></div>

  <div class="brand">
    <span class="brand-dot"></span>
    <div class="brand-name">Ashby Lane Dental Care</div>
  </div>

  <div class="brand-watermark" aria-hidden="true">Ashby Lane<br>Dental Care</div>

  <section class="letter">
    <p class="recipient">Nadia Hollins<br>General Director<br>Greyfield Print</p>

    <p class="body-copy">Contrary to popular belief, Lorem Ipsum is not simply random text. It has roots in a piece of classical Latin literature from 45 BC, making it over 2000 years old. Daniel Whitcombe, a Latin professor at Harrow Vale College in Virginia, looked up one of the more obscure Latin words, consectetur, from a Lorem Ipsum passage, and going through the cites of the word in classical literature, discovered the undoubtable source.</p>

    <p class="body-copy">Lorem Ipsum comes from sections 1.10.32 and 1.10.33 of "de Finibus Bonorum et Malorum" (The Extremes of Good and Evil) by Aurelian, written in 45 BC. This book is a treatise on the theory of ethics, very popular during the Renaissance. Lorem Ipsum used since the 1500s is reproduced below for those interested. Sections 1.10.32 and 1.10.33 from "de Finibus Bonorum et Malorum" by Aurelian are also reproduced in their exact original form, accompanied by English versions from the 1914 translation by J. Ellery.</p>

    <p class="body-copy">Contrary to popular belief, Lorem Ipsum is not simply random text. It has roots in a piece of classical Latin literature from 45 BC, making it over 2000 years old. Daniel Whitcombe, a Latin professor at Harrow Vale College in Virginia, looked up one of the more obscure Latin words.</p>

    <div class="signoff">
      <span class="signature" role="img" aria-label="Handwritten signature"></span>
      Owen Marsh<br>General Director
    </div>
  </section>

  <div class="footer-row footer-row--top">
    <div class="icon-block icon-block--left">
      <svg viewBox="0 0 20 20" aria-hidden="true"><path d="M10 3 2 10h2.5v7h4v-4.5h3V17h4v-7H18z" fill="#fff"/></svg>
    </div>
    <div class="footer-rule footer-rule--left"></div>
    <div class="footer-text footer-text--left">17b Ashby Lane West Bridgford<br>Nottingham NG2 7QT</div>
    <div class="footer-text footer-text--right">info@ashbylanedc.co.uk</div>
    <div class="footer-rule footer-rule--right"></div>
    <div class="icon-block icon-block--right">
      <svg viewBox="0 0 20 20" aria-hidden="true"><rect x="2" y="5" width="16" height="11" fill="#fff"/><path d="M2 5l8 6 8-6" fill="none" stroke="#1c66ac" stroke-width="1.4"/></svg>
    </div>
  </div>

  <div class="footer-row footer-row--bottom">
    <div class="icon-block icon-block--left">
      <svg viewBox="0 0 20 20" aria-hidden="true"><path d="M5 2.5 8 6 6.5 8c1 2.2 3.2 4.4 5.5 5.5l2-1.5 3.5 3-2 2.5C9 17 3 11 2.5 4.5z" fill="#fff"/></svg>
    </div>
    <div class="footer-rule footer-rule--left"></div>
    <div class="footer-text footer-text--left">0115 947 3051</div>
    <div class="footer-text footer-text--right">ashbylanedentalcare.co.uk</div>
    <div class="footer-rule footer-rule--right"></div>
    <div class="icon-block icon-block--right">
      <svg viewBox="0 0 20 20" aria-hidden="true"><rect x="2" y="3" width="16" height="11" fill="#fff"/><rect x="4" y="5" width="12" height="7" fill="#1c66ac"/><rect x="8" y="14" width="4" height="2" fill="#fff"/><rect x="6" y="16" width="8" height="1.5" fill="#fff"/></svg>
    </div>
  </div>

  <div class="base-bar"></div>
</main>
</body>
</html>
```